External Window Signage Design – Antiaging Center

I would like to dress our shop windows in order to promote our activities in medical aesthetics, meso-aesthetics, anti-ageing care and classical beauty. In fact, our 350 m² center is located on the first floor of a building where there is a lot of traffic, as well as a bus stop and metro station. And right in front of a twenty-floor building of the Northern Tariff Bureau.
We want to communicate our activities to our customers with photos and text in a storefront window. So that they can what we do and visit our website www.lumivora.be (our site is in French) as well as our social networks, like picturegram, chatterbook,…
We'd like a window signage : Elegant, Modern, New, Pure, Clean
We are located on the corners of a building, where we have 8 windows on one side and 10 windows on the other, the dimensions are :
Windows
• Height: 125 cm
• Width: 130 cm
Small windows
• Height: 134 cm
• Width: 40 cm
I would say let your imagination go free. I will have other projects for the winner.
Don't hesitate to ask me if you need other formats of the logo or color, like white.
Updates

https://www.pixelbazaar-example.com/design/58204917, I'D LIKE TO HAVE A PROJECT LIKE THIS IF POSSIBLE WITH THE LITTLE WINDOW UNDERNEATH AS WELL.

Target Market(s)

People who want to take care of their external appearance, look beautiful and good looking, womens/girls - mens/boys

Requirements
Must have
• Face and silhouette of a woman. Elegant
Serious, Modern, Professional, Feminine,Upmarket
Nice to have
• To put the different treatments that we propose,
Should not have
• We absolutely don't want a classic beauty center signage, which is reviewed many times

```html
<!DOCTYPE html>
<html lang="fr">
<head>
<meta charset="utf-8">
<title>Lumivora – Habillage de vitrines</title>
<link href="https://fonts.googleapis.com/css2?family=Montserrat:wght@500;700&family=Oswald:wght@400&display=swap" rel="stylesheet">
<style>
  :root {
    --bg: #e4e4e4;
    --gold: #b59c5c;
    --charcoal: #3c3c3c;
    --ink: #2e2e2e;
    --white: #ffffff;
    --panel: #f4f4f4;
  }
  * { box-sizing: border-box; margin: 0; padding: 0; }
  html, body { width: 1200px; height: 400px; overflow: hidden; background: var(--bg); }
  .wall { position: relative; width: 1200px; height: 400px; }

  .windows { position: absolute; left: 55px; top: 119px; display: flex; gap: 10.5px; }
  .window {
    position: relative; width: 127px; height: 121px; overflow: hidden;
    background: linear-gradient(135deg, #ffffff 0%, #eeeeee 60%, #e2e2e2 100%);
  }
  .photo { position: absolute; inset: 0; }
  .photo--group { background: linear-gradient(180deg, #ececec 0%, #d9cfc4 55%, #e6e6e6 100%); }
  .photo--face { background: radial-gradient(circle at 55% 45%, #ecd6c8 0%, #cfc7c3 45%, #bfc3c7 100%); }
  .photo--legs { background: linear-gradient(160deg, #dedede 0%, #d2b49c 50%, #e2e2e2 100%); }
  .photo--reclining { background: linear-gradient(180deg, #e8e8e8 0%, #d8c0ae 55%, #e4e4e4 100%); }
  .wave { position: absolute; left: 0; bottom: 0; width: 100%; height: 100%; }

  .brand { position: absolute; left: 13px; top: 10px; display: flex; align-items: center; gap: 4px; }
  .brand__dot { width: 15px; height: 15px; border-radius: 50%; border: 2px solid var(--gold); }
  .brand__name {
    font-family: "Montserrat", sans-serif; font-weight: 700; font-size: 15.5px;
    color: var(--ink); letter-spacing: -0.4px; line-height: 1;
  }
  .brand__tag {
    position: absolute; left: 46px; top: 28px;
    font-family: "Montserrat", sans-serif; font-weight: 500; font-size: 5px; color: #666;
  }
  .treatments { position: absolute; left: 13px; top: 44px; list-style: none; }
  .treatments li {
    display: flex; align-items: center; gap: 4px;
    font-family: "Montserrat", sans-serif; font-weight: 500; font-size: 6.2px;
    color: var(--ink); line-height: 9.3px; white-space: nowrap;
  }
  .treatments li::before {
    content: ""; width: 3.5px; height: 3.5px; border-radius: 50%; border: 0.8px solid var(--gold);
  }
  .treatments--high { top: 39px; }

  .sills { position: absolute; left: 53px; top: 242px; display: flex; gap: 7.5px; }
  .sill {
    position: relative; width: 130px; height: 39px; background: var(--gold);
    display: flex; flex-direction: column; align-items: center; justify-content: center;
    color: var(--white); overflow: hidden;
  }
  .sill__wave { position: absolute; left: 0; top: 0; width: 100%; height: 14px; }
  .sill__line {
    position: relative; font-family: "Montserrat", sans-serif; font-weight: 500;
    font-size: 8.8px; letter-spacing: 0.6px; line-height: 13px; display: flex; align-items: center; gap: 4px;
  }
  .sill__line--wide { letter-spacing: 1.6px; }
  .sill__line--low { margin-top: 10px; }
  .sill__cond {
    position: relative; font-family: "Oswald", sans-serif; font-weight: 400;
    font-size: 7.6px; line-height: 10px; text-align: center;
  }
  .sill__cond--left { text-align: left; font-size: 8.6px; line-height: 12px; }
  .sill__social { position: relative; margin-top: 10px; font-family: "Montserrat", sans-serif; font-weight: 500; font-size: 6.5px; letter-spacing: 0.4px; }
  .icon { width: 8px; height: 8px; flex: none; }
</style>
</head>
<body>
<div class="wall">

  <div class="windows">
    <div class="window">
      <div class="photo photo--group" role="img" aria-label="Photo de cinq femmes assises sur des chaises de metteur en scène"></div>
      <svg class="wave" viewBox="0 0 127 121" preserveAspectRatio="none" aria-hidden="true">
        <path d="M0 100 C40 92 80 86 127 94 L127 121 L0 121Z" fill="var(--charcoal)"/>
        <path d="M0 108 C40 100 85 98 127 103 L127 121 L0 121Z" fill="var(--white)"/>
        <path d="M0 110 C40 102 85 100 127 105 L127 121 L0 121Z" fill="var(--gold)"/>
      </svg>
    </div>

    <div class="window">
      <div class="brand"><span class="brand__dot"></span><span class="brand__name">Lumivora</span></div>
      <span class="brand__tag">Antiaging Center</span>
      <ul class="treatments">
        <li>SOINS ANTI-ÂGE</li><li>TRAITEMENT DE PEAU</li><li>AMINCISSEMENT &amp; CELLULITE</li>
        <li>TRAITEMENT LASER</li><li>BEAUTÉ ESTHÉTIQUE</li><li>TRAITEMENT COMBINES</li>
      </ul>
      <svg class="wave" viewBox="0 0 127 121" preserveAspectRatio="none" aria-hidden="true">
        <path d="M0 100 C40 102 90 116 127 121 L0 121Z" fill="var(--gold)"/>
        <path d="M60 116 C90 118 110 120 127 121 L127 118 C110 117 90 115 60 116Z" fill="var(--charcoal)"/>
      </svg>
    </div>

    <div class="window">
      <div class="photo photo--face" role="img" aria-label="Photo d'un visage de femme entre des mains gantées"></div>
    </div>

    <div class="window">
      <div class="brand"><span class="brand__dot"></span><span class="brand__name">Lumivora</span></div>
      <span class="brand__tag">Antiaging Center</span>
      <ul class="treatments">
        <li>SKIN RÉJUVÉNATION</li><li>LIFTING VISAGE</li><li>THERMALINE</li>
        <li>HIFU</li><li>HYDRACLAIR</li><li>SOLANE ADN</li>
      </ul>
      <svg class="wave" viewBox="0 0 127 121" preserveAspectRatio="none" aria-hidden="true">
        <path d="M60 121 C90 116 110 112 127 108 L127 121Z" fill="var(--charcoal)"/>
      </svg>
    </div>

    <div class="window">
      <div class="photo photo--legs" role="img" aria-label="Photo d'une silhouette de femme allongée, jambes relevées"></div>
      <svg class="wave" viewBox="0 0 127 121" preserveAspectRatio="none" aria-hidden="true">
        <path d="M0 100 C40 94 85 92 127 96 L127 121 L0 121Z" fill="var(--charcoal)"/>
        <path d="M0 107 C40 102 85 102 127 104 L127 121 L0 121Z" fill="var(--white)"/>
        <path d="M0 109 C40 104 85 104 127 106 L127 121 L0 121Z" fill="var(--gold)"/>
      </svg>
    </div>

    <div class="window">
      <div class="photo photo--reclining" role="img" aria-label="Photo d'une femme allongée en lingerie blanche"></div>
      <svg class="wave" viewBox="0 0 127 121" preserveAspectRatio="none" aria-hidden="true">
        <path d="M0 98 C40 96 85 100 127 110 L127 121 L0 121Z" fill="var(--charcoal)"/>
        <path d="M0 106 C40 104 85 108 127 116 L127 121 L0 121Z" fill="var(--white)"/>
        <path d="M0 108 C40 106 85 110 127 118 L127 121 L0 121Z" fill="var(--gold)"/>
      </svg>
    </div>

    <div class="window">
      <div class="brand"><span class="brand__dot"></span><span class="brand__name">Lumivora</span></div>
      <span class="brand__tag">Antiaging Center</span>
      <ul class="treatments">
        <li>ANALYSE DE PEAU</li><li>TRAITEMENT ACNÉ</li><li>TACHE PIGMENTAIRE</li>
        <li>PEELING</li><li>HYDRACLAIR</li><li>TRAITEMENTS ESTHÉTIQUES</li>
      </ul>
    </div>

    <div class="window">
      <div class="brand"><span class="brand__dot"></span><span class="brand__name">Lumivora</span></div>
      <span class="brand__tag">Antiaging Center</span>
      <ul class="treatments treatments--high">
        <li>ÉPILATION LASER À FROID</li><li>LIPOCAVITATION</li><li>MÉSOTHÉRAPIE</li>
        <li>LIPOLASER</li><li>ANTICELLULITE</li><li>LUMINOTHÉRAPIE</li>
      </ul>
      <svg class="wave" viewBox="0 0 127 121" preserveAspectRatio="none" aria-hidden="true">
        <path d="M0 121 C30 104 80 96 127 98 L127 121Z" fill="var(--charcoal)"/>
        <path d="M0 121 C30 108 80 102 127 105 L127 121Z" fill="var(--white)"/>
        <path d="M0 121 C30 110 80 104 127 107 L127 121Z" fill="var(--gold)"/>
      </svg>
    </div>
  </div>

  <div class="sills">
    <div class="sill">
      <span class="sill__line"><svg class="icon" viewBox="0 0 10 10" aria-hidden="true"><rect x="1" y="2.5" width="8" height="5.5" fill="none" stroke="#fff" stroke-width="0.8"/><path d="M1 2.5 L5 5.5 L9 2.5" fill="none" stroke="#fff" stroke-width="0.8"/></svg>info@lumivora.be</span>
      <span class="sill__line"><svg class="icon" viewBox="0 0 10 10" aria-hidden="true"><circle cx="5" cy="5" r="4.3" fill="none" stroke="#fff" stroke-width="0.8"/><path d="M3.4 2.8 L4.3 3.8 L3.9 4.5 Q4.6 5.8 5.6 6.2 L6.2 5.7 L7.2 6.6 L6.5 7.4 Q3.6 6.8 2.7 3.5Z" fill="#fff"/></svg>+32 (0)2 000 14 27</span>
    </div>

    <div class="sill">
      <svg class="sill__wave" viewBox="0 0 130 14" preserveAspectRatio="none" aria-hidden="true">
        <path d="M0 0 L130 0 L130 4 C100 4 60 2 0 0Z" fill="var(--white)"/>
        <path d="M100 3 C115 4 125 5 130 6 L130 4Z" fill="var(--charcoal)"/>
      </svg>
      <span class="sill__line sill__line--wide"><svg class="icon" viewBox="0 0 10 10" aria-hidden="true"><circle cx="5" cy="5" r="4" fill="none" stroke="#fff" stroke-width="0.8"/><path d="M1 5 H9 M5 1 Q2.5 5 5 9 M5 1 Q7.5 5 5 9" fill="none" stroke="#fff" stroke-width="0.7"/></svg>www.lumivora.be</span>
    </div>

    <div class="sill">
      <svg class="sill__wave" viewBox="0 0 130 14" preserveAspectRatio="none" aria-hidden="true">
        <path d="M0 0 L130 0 L130 12 C90 6 40 4 0 4Z" fill="var(--white)"/>
        <path d="M0 4 C40 4 90 6 130 12 L130 14 C90 9 40 8 0 9Z" fill="var(--charcoal)"/>
      </svg>
      <span class="sill__social">chatterbook · picturegram</span>
    </div>

    <div class="sill">
      <svg class="sill__wave" viewBox="0 0 130 14" preserveAspectRatio="none" aria-hidden="true">
        <path d="M0 14 C40 8 90 4 130 0 L0 0Z" fill="var(--charcoal)"/>
        <path d="M0 14 C40 9 90 6 130 3 L130 0 C90 4 40 8 0 12Z" fill="var(--white)"/>
      </svg>
      <span class="sill__line sill__line--wide sill__line--low"><svg class="icon" viewBox="0 0 10 10" aria-hidden="true"><circle cx="5" cy="5" r="4" fill="none" stroke="#fff" stroke-width="0.8"/><path d="M1 5 H9 M5 1 Q2.5 5 5 9 M5 1 Q7.5 5 5 9" fill="none" stroke="#fff" stroke-width="0.7"/></svg>www.lumivora.be</span>
    </div>

    <div class="sill">
      <span class="sill__cond">Place Verdelle,<br>Avenue des Lys 14, Premier étage<br>1210 Bruxelles</span>
    </div>

    <div class="sill">
      <span class="sill__cond sill__cond--left">BIENVENUE DANS NOTRE<br>TOUT NOUVEAU CENTRE À VERDELLE</span>
    </div>

    <div class="sill">
      <svg class="sill__wave" viewBox="0 0 130 14" preserveAspectRatio="none" aria-hidden="true">
        <path d="M0 0 L130 0 L130 2 C90 6 40 8 0 9Z" fill="var(--white)"/>
        <path d="M0 9 C40 8 90 6 130 2 L130 5 C90 9 40 12 0 13Z" fill="var(--charcoal)"/>
      </svg>
      <span class="sill__line sill__line--wide sill__line--low"><svg class="icon" viewBox="0 0 10 10" aria-hidden="true"><circle cx="5" cy="5" r="4" fill="none" stroke="#fff" stroke-width="0.8"/><path d="M1 5 H9 M5 1 Q2.5 5 5 9 M5 1 Q7.5 5 5 9" fill="none" stroke="#fff" stroke-width="0.7"/></svg>www.lumivora.be</span>
    </div>

    <div class="sill">
      <span class="sill__line"><svg class="icon" viewBox="0 0 10 10" aria-hidden="true"><rect x="1" y="2.5" width="8" height="5.5" fill="none" stroke="#fff" stroke-width="0.8"/><path d="M1 2.5 L5 5.5 L9 2.5" fill="none" stroke="#fff" stroke-width="0.8"/></svg>info@lumivora.be</span>
      <span class="sill__line"><svg class="icon" viewBox="0 0 10 10" aria-hidden="true"><circle cx="5" cy="5" r="4.3" fill="none" stroke="#fff" stroke-width="0.8"/><path d="M3.4 2.8 L4.3 3.8 L3.9 4.5 Q4.6 5.8 5.6 6.2 L6.2 5.7 L7.2 6.6 L6.5 7.4 Q3.6 6.8 2.7 3.5Z" fill="#fff"/></svg>+32 (0)2 000 14 27</span>
    </div>
  </div>

</div>
</body>
</html>
```